Auto parts webshop needs a webdesign

We need a webdesign for https://www.vornik.nl/. Vornik delivers parts, Accessories, Rims, Tires, Exhausts for USA cars and old timers. We would like to have a home page to start with. Then, after evaluating, in the second round, we would like a productoverview, productdetail page and a general information page, like about us.
Below some points:
- It's a combination of business to business and business to consumer. So login / registration is necassary | maybe a block on the home page with a button to the a registration page and a text like: registrate to get special discounts and prices
- Shopping cart
- Fixed header
- Mega menu
- Search and filtering (use dummy data)
- Categories: a) based on brands b) based parts
- Colors: color of logo #ff0000 and blue. It doesnt need to be flashy, but somehow professional.
Below 2 sites Vornik likes:
1. https://www.quell-onderdelen.nl/
"They have an set up more or less similar to what we want."
2. https://www.zatrowerk.com/nl/
"clear and also no nonsense"
Below some designs we already implemented so you can see the functionalities / designgrid:
1. https://pemlisa.nl/
2. https://www.grunvale.com/
Target Market(s)
Parts, Accessories, Rims, Tires, Exhausts for USA cars and old timers
Industry/Entity Type
Spare parts cars
Number of Pages Required
4 page
Font styles to use
Colors
Designer to choose colors to be used in the design.
Look and feel

```html
<!DOCTYPE html>
<html lang="en">
<head>
<meta charset="utf-8">
<title>Vornik – Auto parts webshop</title>
<link href="https://fonts.googleapis.com/css2?family=Poppins:wght@400;500;600;700;800&display=swap" rel="stylesheet">
<style>
:root{
  --red:#e31e24;
  --ink:#1b1b1b;
  --dark:#161616;
  --dark-2:#242424;
  --grey-bg:#f2f2f2;
  --muted:#777;
  --white:#ffffff;
  --star:#f5b400;
  --blue:#2b3bd1;
  --pic:#e6e6e6;
}
*{box-sizing:border-box;margin:0;padding:0}
html,body{width:1200px;height:5132px;overflow:hidden}
body{font-family:"Poppins",sans-serif;color:var(--ink);background:var(--grey-bg);position:relative}
.block{position:absolute;left:0;width:1200px}
.wrap{position:absolute;left:124px;width:952px}

/* top bar */
.topbar{top:0;height:72px;background:var(--dark);color:var(--white);font-size:13px;font-weight:500;letter-spacing:.3px}
.topbar .welcome{position:absolute;left:124px;top:26px;text-transform:uppercase}
.topbar .follow{position:absolute;left:600px;top:26px;display:flex;align-items:center;gap:10px;text-transform:uppercase}
.topbar .follow .sep{width:1px;height:18px;background:#666;margin-right:8px}
.dot{width:16px;height:16px;border-radius:50%;background:var(--white);display:inline-block}
.topbar .login{position:absolute;right:124px;top:18px;height:36px;padding:0 14px;border:1px solid #555;display:flex;align-items:center;gap:8px;text-transform:uppercase}

/* header */
.header{top:72px;height:176px;background:var(--white)}
.logo{position:absolute;left:124px;top:60px;font-size:48px;font-weight:800;color:var(--red);letter-spacing:1px;line-height:1}
.search{position:absolute;left:368px;top:64px;width:432px;height:56px;border:1px solid #bbb;font-size:15px;color:#888;padding:16px 18px}
.search-btn{position:absolute;left:808px;top:64px;width:56px;height:56px;background:var(--dark-2);display:flex;align-items:center;justify-content:center}
.header .icon{position:absolute;top:76px}

/* nav */
.nav{top:248px;height:112px;background:var(--red);color:var(--white)}
.browse{position:absolute;left:124px;top:0;width:276px;height:112px;background:var(--dark-2);display:flex;align-items:center;gap:16px;padding-left:24px;font-size:18px;font-weight:500}
.menu{position:absolute;left:436px;top:40px;display:flex;gap:34px;font-size:19px;font-weight:700}
.phone{position:absolute;right:124px;top:30px;display:flex;align-items:center;gap:16px;font-size:30px;font-weight:700}
.phone .ring{width:52px;height:52px;border-radius:50%;border:2px solid var(--white);display:flex;align-items:center;justify-content:center}

/* hero */
.hero{top:360px;height:620px;background:linear-gradient(90deg,#121212 0%,#1c1c1c 45%,#2a2a2a 100%)}
.hero-photo{position:absolute;left:560px;top:0;width:640px;height:620px;background:radial-gradient(ellipse at 60% 55%,#4a4a4a 0%,#2a2a2a 50%,#161616 85%)}
.hero-copy{position:absolute;left:124px;top:40px;width:520px;color:var(--white)}
.eyebrow{color:var(--red);font-size:17px;font-weight:500}
.hero h1{font-size:48px;font-weight:700;margin-top:8px;line-height:1.2}
.hero .lead{font-size:27px;line-height:1.35;margin-top:28px;font-weight:400}
.hero .register-note{font-size:25px;font-weight:700;line-height:1.4;margin-top:64px}
.hero .actions{display:flex;align-items:center;gap:48px;margin-top:44px}
.btn{background:var(--red);color:var(--white);font-weight:700;display:inline-flex;align-items:center;justify-content:center}
.btn-login{width:172px;height:68px;font-size:22px}
.link-register{color:var(--red);font-size:22px;font-weight:700}

/* promo cards */
.promos{display:flex;gap:20px}
.promo{position:relative;width:304px;background:#2b2b2b;overflow:hidden;color:var(--white)}
.promo .shot{position:absolute;right:0;top:0;width:170px;height:100%;background:linear-gradient(90deg,#2b2b2b,#4a4a4a)}
.promo .txt{position:absolute;left:22px;top:26px}
.promo .tag{font-size:12px;font-weight:500;display:flex;gap:6px}
.promo .tag b{color:var(--red);font-weight:600}
.promo .title{font-size:34px;font-weight:700;line-height:1.2;margin-top:2px}
.promo .price{font-size:18px;margin-top:18px}
.promo .price b{color:var(--red);font-size:26px;font-weight:700}
.promo .add{position:absolute;left:22px;width:88px;height:30px;font-size:11px}

/* section heading */
.sec-head{display:flex;align-items:center;gap:18px;font-size:31px;font-weight:500}
.sec-head::before{content:"";width:34px;height:3px;background:var(--ink)}

/* products */
.grid{display:grid;grid-template-columns:repeat(4,226px);gap:40px 16px}
.card{position:relative;height:328px;background:var(--white);overflow:hidden}
.card .pic{position:absolute;left:30px;top:20px;width:166px;height:130px;border-radius:6px;background:linear-gradient(180deg,#efefef,var(--pic))}
.card h3{position:absolute;left:18px;top:166px;font-size:20px;font-weight:700}
.card p{position:absolute;left:18px;top:200px;width:196px;font-size:13px;color:var(--muted);line-height:1.5}
.card .stars{position:absolute;left:18px;top:252px;font-size:16px;color:var(--star);letter-spacing:1px}
.card .stars i{font-style:normal;color:#ccc}
.card .cart{position:absolute;left:16px;top:286px}
.card .price{position:absolute;right:0;top:286px;width:96px;height:34px;background:var(--red);color:var(--white);font-weight:700;font-size:17px;display:flex;align-items:center;justify-content:center}

/* black november banner */
.deal{top:2192px;height:428px;background:linear-gradient(90deg,#151515,#262626 60%,#1b1b1b)}
.deal .art{position:absolute;left:40px;top:60px;width:520px;height:300px;background:radial-gradient(ellipse at 50% 50%,#3a2020 0%,#262626 55%,transparent 80%)}
.deal .copy{position:absolute;left:628px;top:72px;width:290px;color:var(--white);font-size:19px;line-height:1.5}
.deal .read{position:absolute;left:634px;top:256px;width:168px;height:64px;font-size:20px}

/* brands */
.brands{top:3940px;height:168px}
.brand-row{position:absolute;left:124px;top:0;display:flex;gap:17px}
.brand{width:144px;height:168px;background:var(--white);display:flex;flex-direction:column;align-items:center;justify-content:center;gap:10px;font-size:17px;font-weight:700;color:var(--ink)}
.brand.shade{background:#e3e3e3}
.brand .mark{width:46px;height:46px;border-radius:50%;background:var(--red)}
.arrow{position:absolute;top:66px;width:24px;height:36px;background:var(--red);display:flex;align-items:center;justify-content:center}

/* about */
.about{top:4140px;height:400px}
.about .photo{position:absolute;left:124px;top:0;width:396px;height:380px;border-radius:6px;background:radial-gradient(ellipse at 50% 60%,#8a2226 0%,#3b1416 40%,#121212 75%)}
.about h2{position:absolute;left:544px;top:18px;font-size:30px;font-weight:700}
.about p{position:absolute;left:544px;top:76px;width:532px;font-size:14px;line-height:1.75;color:#444}

/* footer */
.footer{top:4600px;height:532px;background:#151515;color:var(--white)}
.footer .tools{position:absolute;right:0;top:0;width:460px;height:532px;background:radial-gradient(ellipse at 70% 60%,#4a3a2a 0%,#2a2520 45%,#151515 80%)}
.footer .col{position:absolute;top:104px}
.footer h4{color:var(--red);font-size:22px;font-weight:600;margin-bottom:16px}
.footer .col p,.footer .col li{font-size:16px;line-height:1.75;list-style:none}
.footer .col .red{color:var(--red)}
.footer .socials{display:flex;gap:10px;margin-bottom:16px}
.footer .socials .dot{width:20px;height:20px}
.footer .copy{position:absolute;left:124px;top:488px;font-size:15px}
.footer .copy b{color:var(--red);font-weight:500}
.footer .rule{position:absolute;left:0;top:460px;width:1200px;height:1px;background:#333}
</style>
</head>
<body>

<div class="block topbar">
  <div class="welcome">Welcome to Vornik online shopping store</div>
  <div class="follow"><span class="sep"></span>Follow us <span class="dot" aria-label="Social profile"></span><span class="dot" aria-label="Social profile"></span><span class="dot" aria-label="Social profile"></span></div>
  <div class="login">
    <svg width="16" height="16" viewBox="0 0 16 16"><circle cx="8" cy="5" r="3.2" fill="#fff"/><path d="M1.5 15c0-3.6 3-5.5 6.5-5.5s6.5 1.9 6.5 5.5z" fill="#fff"/></svg>
    Login / Signup
  </div>
</div>

<header class="block header">
  <div class="logo">VORNIK</div>
  <div class="search">Search here...</div>
  <div class="search-btn"><svg width="26" height="26" viewBox="0 0 26 26"><circle cx="11" cy="11" r="7.5" stroke="#fff" stroke-width="2.6" fill="none"/><line x1="16.5" y1="16.5" x2="23" y2="23" stroke="#fff" stroke-width="2.8" stroke-linecap="round"/></svg></div>
  <svg class="icon" style="left:990px" width="34" height="32" viewBox="0 0 34 32"><path d="M17 29 4.5 16.5A7.5 7.5 0 0 1 17 6a7.5 7.5 0 0 1 12.5 10.5z" fill="none" stroke="#1b1b1b" stroke-width="2.6"/></svg>
  <svg class="icon" style="left:1044px" width="34" height="32" viewBox="0 0 34 32"><path d="M2 4h5l4 17h16l4-12H9" fill="none" stroke="#1b1b1b" stroke-width="2.6" stroke-linejoin="round"/><circle cx="13" cy="27" r="2.5" fill="#1b1b1b"/><circle cx="25" cy="27" r="2.5" fill="#1b1b1b"/></svg>
</header>

<nav class="block nav">
  <div class="browse">
    <svg width="22" height="18" viewBox="0 0 22 18"><rect y="1" width="22" height="2.5" fill="#fff"/><rect y="8" width="22" height="2.5" fill="#fff"/><rect y="15" width="22" height="2.5" fill="#fff"/></svg>
    Browse Categories
    <svg width="14" height="10" viewBox="0 0 14 10" style="margin-left:14px"><path d="M2 2l5 5 5-5" stroke="#fff" stroke-width="2" fill="none"/></svg>
  </div>
  <div class="menu"><span>Home</span><span>Shop</span><span>About</span><span>Contact</span></div>
  <div class="phone">
    <span class="ring"><svg width="24" height="24" viewBox="0 0 24 24"><path d="M6.6 10.8a15 15 0 0 0 6.6 6.6l2.2-2.2a1 1 0 0 1 1-.25 11.4 11.4 0 0 0 3.6.6 1 1 0 0 1 1 1V20a1 1 0 0 1-1 1A17 17 0 0 1 3 4a1 1 0 0 1 1-1h3.5a1 1 0 0 1 1 1c0 1.25.2 2.45.6 3.6a1 1 0 0 1-.25 1z" fill="#fff"/></svg></span>
    030-415 7720
  </div>
</nav>

<section class="block hero">
  <div class="hero-photo" role="img" aria-label="Black sports car parked in a dim workshop"></div>
  <div class="hero-copy">
    <div class="eyebrow">Welcome to Vornik Parts Digital!</div>
    <h1>Auto parts webshop</h1>
    <p class="lead">Vornik delivers parts, Accessories, Rims, Tires, Exhausts for USA cars and old timers</p>
    <p class="register-note">Registrate to get special discounts and prices</p>
    <div class="actions"><span class="btn btn-login">Login</span><span class="link-register">Register</span></div>
  </div>
</section>

<div class="wrap promos" style="top:1052px;height:248px">
  <div class="promo"><div class="shot" role="img" aria-label="Brake disc and caliper"></div><div class="txt"><div class="tag">Limit And <b>Offer</b></div><div class="title">Mega Sale</div><div class="price">Price: <b>$500.00</b></div></div><span class="btn add" style="top:176px">Add to cart</span></div>
  <div class="promo"><div class="shot" role="img" aria-label="Engine parts"></div><div class="txt"><div class="tag">Body Parts</div><div class="title">Mega Sale</div><div class="price">Price: <b>$500.00</b></div></div><span class="btn add" style="top:176px">Add to cart</span></div>
  <div class="promo"><div class="shot" role="img" aria-label="Engine block"></div><div class="txt"><div class="tag">Engin Parts <b>Offer</b></div><div class="title">Mega Sale</div><div class="price">Price: <b>$500.00</b></div></div><span class="btn add" style="top:176px">Add to cart</span></div>
</div>

<h2 class="wrap sec-head" style="top:1368px">New Arrivals</h2>

<div class="wrap grid" style="top:1440px">
  <div class="card"><div class="pic" role="img" aria-label="Alternator"></div><h3>Lorem Ipsum</h3><p>Fermentum, aliquam sed volutpat consequat sagittis.</p><div class="stars">★★★<i>★★</i></div><svg class="cart" width="26" height="24" viewBox="0 0 26 24"><path d="M1 2h4l3 13h12l3-9H7" fill="none" stroke="#2b3bd1" stroke-width="2.2"/><circle cx="10" cy="20" r="2" fill="#2b3bd1"/><circle cx="19" cy="20" r="2" fill="#2b3bd1"/></svg><div class="price">$209.45</div></div>
  <div class="card"><div class="pic" role="img" aria-label="Shock absorber"></div><h3>Lorem Ipsum</h3><p>Fermentum, aliquam sed volutpat consequat sagittis.</p><div class="stars">★★★<i>★★</i></div><svg class="cart" width="26" height="24" viewBox="0 0 26 24"><path d="M1 2h4l3 13h12l3-9H7" fill="none" stroke="#2b3bd1" stroke-width="2.2"/><circle cx="10" cy="20" r="2" fill="#2b3bd1"/><circle cx="19" cy="20" r="2" fill="#2b3bd1"/></svg><div class="price">$209.45</div></div>
  <div class="card"><div class="pic" role="img" aria-label="Tire on rim"></div><h3>Lorem Ipsum</h3><p>Fermentum, aliquam sed volutpat consequat sagittis.</p><div class="stars">★★★<i>★★</i></div><svg class="cart" width="26" height="24" viewBox="0 0 26 24"><path d="M1 2h4l3 13h12l3-9H7" fill="none" stroke="#2b3bd1" stroke-width="2.2"/><circle cx="10" cy="20" r="2" fill="#2b3bd1"/><circle cx="19" cy="20" r="2" fill="#2b3bd1"/></svg><div class="price">$209.45</div></div>
  <div class="card"><div class="pic" role="img" aria-label="Car battery"></div><h3>Lorem Ipsum</h3><p>Fermentum, aliquam sed volutpat consequat sagittis.</p><div class="stars">★★★<i>★★</i></div><svg class="cart" width="26" height="24" viewBox="0 0 26 24"><path d="M1 2h4l3 13h12l3-9H7" fill="none" stroke="#2b3bd1" stroke-width="2.2"/><circle cx="10" cy="20" r="2" fill="#2b3bd1"/><circle cx="19" cy="20" r="2" fill="#2b3bd1"/></svg><div class="price">$209.45</div></div>
  <div class="card"><div class="pic" role="img" aria-label="Engine component"></div><h3>Lorem Ipsum</h3><p>Fermentum, aliquam sed volutpat consequat sagittis.</p><div class="stars">★★★<i>★★</i></div><svg class="cart" width="26" height="24" viewBox="0 0 26 24"><path d="M1 2h4l3 13h12l3-9H7" fill="none" stroke="#2b3bd1" stroke-width="2.2"/><circle cx="10" cy="20" r="2" fill="#2b3bd1"/><circle cx="19" cy="20" r="2" fill="#2b3bd1"/></svg><div class="price">$209.45</div></div>
  <div class="card"><div class="pic" role="img" aria-label="Motor oil bottles"></div><h3>Lorem Ipsum</h3><p>Fermentum, aliquam sed volutpat consequat sagittis.</p><div class="stars">★★★<i>★★</i></div><svg class="cart" width="26" height="24" viewBox="0 0 26 24"><path d="M1 2h4l3 13h12l3-9H7" fill="none" stroke="#2b3bd1" stroke-width="2.2"/><circle cx="10" cy="20" r="2" fill="#2b3bd1"/><circle cx="19" cy="20" r="2" fill="#2b3bd1"/></svg><div class="price">$209.45</div></div>
  <div class="card"><div class="pic" role="img" aria-label="Chrome car emblem"></div><h3>Lorem Ipsum</h3><p>Fermentum, aliquam sed volutpat consequat sagittis.</p><div class="stars">★★★<i>★★</i></div><svg class="cart" width="26" height="24" viewBox="0 0 26 24"><path d="M1 2h4l3 13h12l3-9H7" fill="none" stroke="#2b3bd1" stroke-width="2.2"/><circle cx="10" cy="20" r="2" fill="#2b3bd1"/><circle cx="19" cy="20" r="2" fill="#2b3bd1"/></svg><div class="price">$209.45</div></div>
  <div class="card"><div class="pic" role="img" aria-label="Brake assembly"></div><h3>Lorem Ipsum</h3><p>Fermentum, aliquam sed volutpat consequat sagittis.</p><div class="stars">★★★<i>★★</i></div><svg class="cart" width="26" height="24" viewBox="0 0 26 24"><path d="M1 2h4l3 13h12l3-9H7" fill="none" stroke="#2b3bd1" stroke-width="2.2"/><circle cx="10" cy="20" r="2" fill="#2b3bd1"/><circle cx="19" cy="20" r="2" fill="#2b3bd1"/></svg><div class="price">$209.45</div></div>
</div>

<section class="wrap deal">
  <div class="art" role="img" aria-label="Black November sale lettering"></div>
  <p class="copy">Fermentum, aliquam sed volutpat consequat sagittis duis donec neque. Libero feugiat id tempus mis, massa facilisis euismod tellus.</p>
  <span class="btn read">Read more</span>
</section>

<div class="wrap promos" style="top:2648px;height:240px">
  <div class="promo"><div class="shot" role="img" aria-label="Brake disc and caliper"></div><div class="txt"><div class="tag">Limit And <b>Offer</b></div><div class="title">Mega Sale</div><div class="price">Price: <b>$500.00</b></div></div><span class="btn add" style="top:172px">Add to cart</span></div>
  <div class="promo"><div class="shot" role="img" aria-label="Engine parts"></div><div class="txt"><div class="tag">Body Parts</div><div class="title">Mega Sale</div><div class="price">Price: <b>$500.00</b></div></div><span class="btn add" style="top:172px">Add to cart</span></div>
  <div class="promo"><div class="shot" role="img" aria-label="Engine block"></div><div class="txt"><div class="tag">Engin Parts <b>Offer</b></div><div class="title">Mega Sale</div><div class="price">Price: <b>$500.00</b></div></div><span class="btn add" style="top:172px">Add to cart</span></div>
</div>

<h2 class="wrap sec-head" style="top:2960px">Price $100 to $500</h2>

<div class="wrap grid" style="top:3032px">
  <div class="card"><div class="pic" role="img" aria-label="Alternator"></div><h3>Lorem Ipsum</h3><p>Fermentum, aliquam sed volutpat consequat sagittis.</p><div class="stars">★★★<i>★★</i></div><svg class="cart" width="26" height="24" viewBox="0 0 26 24"><path d="M1 2h4l3 13h12l3-9H7" fill="none" stroke="#2b3bd1" stroke-width="2.2"/><circle cx="10" cy="20" r="2" fill="#2b3bd1"/><circle cx="19" cy="20" r="2" fill="#2b3bd1"/></svg><div class="price">$209.45</div></div>
  <div class="card"><div class="pic" role="img" aria-label="Shock absorber"></div><h3>Lorem Ipsum</h3><p>Fermentum, aliquam sed volutpat consequat sagittis.</p><div class="stars">★★★<i>★★</i></div><svg class="cart" width="26" height="24" viewBox="0 0 26 24"><path d="M1 2h4l3 13h12l3-9H7" fill="none" stroke="#2b3bd1" stroke-width="2.2"/><circle cx="10" cy="20" r="2" fill="#2b3bd1"/><circle cx="19" cy="20" r="2" fill="#2b3bd1"/></svg><div class="price">$209.45</div></div>
  <div class="card"><div class="pic" role="img" aria-label="Tire on rim"></div><h3>Lorem Ipsum</h3><p>Fermentum, aliquam sed volutpat consequat sagittis.</p><div class="stars">★★★<i>★★</i></div><svg class="cart" width="26" height="24" viewBox="0 0 26 24"><path d="M1 2h4l3 13h12l3-9H7" fill="none" stroke="#2b3bd1" stroke-width="2.2"/><circle cx="10" cy="20" r="2" fill="#2b3bd1"/><circle cx="19" cy="20" r="2" fill="#2b3bd1"/></svg><div class="price">$209.45</div></div>
  <div class="card"><div class="pic" role="img" aria-label="Car battery"></div><h3>Lorem Ipsum</h3><p>Fermentum, aliquam sed volutpat consequat sagittis.</p><div class="stars">★★★<i>★★</i></div><svg class="cart" width="26" height="24" viewBox="0 0 26 24"><path d="M1 2h4l3 13h12l3-9H7" fill="none" stroke="#2b3bd1" stroke-width="2.2"/><circle cx="10" cy="20" r="2" fill="#2b3bd1"/><circle cx="19" cy="20" r="2" fill="#2b3bd1"/></svg><div class="price">$209.45</div></div>
</div>

<h2 class="wrap sec-head" style="top:3408px">Price $500 to $1000</h2>

<div class="wrap grid" style="top:3472px">
  <div class="card"><div class="pic" role="img" aria-label="Alternator"></div><h3>Lorem Ipsum</h3><p>Fermentum, aliquam sed volutpat consequat sagittis.</p><div class="stars">★★★<i>★★</i></div><svg class="cart" width="26" height="24" viewBox="0 0 26 24"><path d="M1 2h4l3 13h12l3-9H7" fill="none" stroke="#2b3bd1" stroke-width="2.2"/><circle cx="10" cy="20" r="2" fill="#2b3bd1"/><circle cx="19" cy="20" r="2" fill="#2b3bd1"/></svg><div class="price">$209.45</div></div>
  <div class="card"><div class="pic" role="img" aria-label="Shock absorber"></div><h3>Lorem Ipsum</h3><p>Fermentum, aliquam sed volutpat consequat sagittis.</p><div class="stars">★★★<i>★★</i></div><svg class="cart" width="26" height="24" viewBox="0 0 26 24"><path d="M1 2h4l3 13h12l3-9H7" fill="none" stroke="#2b3bd1" stroke-width="2.2"/><circle cx="10" cy="20" r="2" fill="#2b3bd1"/><circle cx="19" cy="20" r="2" fill="#2b3bd1"/></svg><div class="price">$209.45</div></div>
  <div class="card"><div class="pic" role="img" aria-label="Tire on rim"></div><h3>Lorem Ipsum</h3><p>Fermentum, aliquam sed volutpat consequat sagittis.</p><div class="stars">★★★<i>★★</i></div><svg class="cart" width="26" height="24" viewBox="0 0 26 24"><path d="M1 2h4l3 13h12l3-9H7" fill="none" stroke="#2b3bd1" stroke-width="2.2"/><circle cx="10" cy="20" r="2" fill="#2b3bd1"/><circle cx="19" cy="20" r="2" fill="#2b3bd1"/></svg><div class="price">$209.45</div></div>
  <div class="card"><div class="pic" role="img" aria-label="Car battery"></div><h3>Lorem Ipsum</h3><p>Fermentum, aliquam sed volutpat consequat sagittis.</p><div class="stars">★★★<i>★★</i></div><svg class="cart" width="26" height="24" viewBox="0 0 26 24"><path d="M1 2h4l3 13h12l3-9H7" fill="none" stroke="#2b3bd1" stroke-width="2.2"/><circle cx="10" cy="20" r="2" fill="#2b3bd1"/><circle cx="19" cy="20" r="2" fill="#2b3bd1"/></svg><div class="price">$209.45</div></div>
</div>

<h2 class="wrap sec-head" style="top:3864px">We deals in this brands</h2>

<section class="block brands">
  <span class="arrow" style="left:96px"><svg width="10" height="14" viewBox="0 0 10 14"><path d="M8 1 2 7l6 6" stroke="#fff" stroke-width="2.2" fill="none"/></svg></span>
  <div class="brand-row">
    <div class="brand"><span class="mark"></span>Autolane</div>
    <div class="brand">Ardent</div>
    <div class="brand"><span class="mark"></span>Brisko</div>
    <div class="brand shade"><span class="mark"></span>Oltra</div>
    <div class="brand"><span class="mark"></span>Ferrox</div>
    <div class="brand"><span class="mark"></span>Geardo</div>
  </div>
  <span class="arrow" style="left:1080px"><svg width="10" height="14" viewBox="0 0 10 14"><path d="M2 1l6 6-6 6" stroke="#fff" stroke-width="2.2" fill="none"/></svg></span>
</section>

<section class="block about">
  <div class="photo" role="img" aria-label="Dark sports car under red light"></div>
  <h2>About VORNIK</h2>
  <p>In our programme you will find all that you need for your USA car: bumpers, body panels, headlamps, engine parts, exhausts, rims, tyres and electrical parts. Besides that we carry a wide range of accessories and workshop tools. Are you unable to find the part you need? Send us your request and we will gladly search for it. Our team is ready to help with quick advice, fair prices and reliable delivery, so your classic or modern car stays on the road.</p>
</section>

<footer class="block footer">
  <div class="tools" role="img" aria-label="Wrenches and workshop tools"></div>
  <div class="col" style="left:124px;width:300px">
    <h4>Location</h4>
    <p>Fermentum, aliquam sed volutpat consequat sagittis duis donec neque. Libero feugiat id tempus mis, massa facilisis euismod tellus.</p>
    <p style="margin-top:10px"><span class="red">Email:</span> abc@postmail.nl</p>
    <p><span class="red">phone:</span> 00044556677</p>
  </div>
  <div class="col" style="left:536px">
    <h4>Quick links</h4>
    <ul><li>Home</li><li>Profile</li><li>Shop</li><li>Brands</li><li>Pricing</li><li>Contact Us</li></ul>
  </div>
  <div class="col" style="left:830px;width:200px">
    <h4>Follow Us</h4>
    <div class="socials"><span class="dot" aria-label="Social profile"></span><span class="dot" aria-label="Social profile"></span><span class="dot" aria-label="Social profile"></span></div>
    <p>Fermentum, aliquam sed volutpat consequat sagittis.</p>
  </div>
  <div class="rule"></div>
  <div class="copy">All right reserved 2022. <b>Vornik</b></div>
</footer>

</body>
</html>
```